Stump Grinding sidewalk sign

I have an A-frame sign that has a 24" x 36" flat area for a vinyl sign to be applied to. the sign can also be applied to sheet metal and then screwed to the A-frame sign.
I have included a few pictures of my logo, the A-frame, and my business card.

Target Market(s)

Tree and stump industry

Font styles to use
Decorative

Requirements
Must have
• I would like my company name , logo, slogan, and phone number on the sign. Along with "Fully Insured" and "free Estimates".
The sign is black, and I would like bright colors such as safety green and/or neon yellow. Or possibly a florescent red?
Nice to have
• Some sort of background to break up the blank "solidness"

```html
<!DOCTYPE html>
<html lang="en">
<head>
<meta charset="UTF-8">
<title>Barlow's Stump Grinding – Sidewalk Sign</title>
<link href="https://fonts.googleapis.com/css2?family=Oswald:wght@500;600;700&family=Archivo:wght@800&display=swap" rel="stylesheet">
<style>
  :root {
    --page-bg: #eeeeee;
    --green-light: #9ccf3c;
    --green-mid: #5cb531;
    --green-deep: #2f9a35;
    --green-ink: #1f5a2c;
    --white: #ffffff;
    --band-white: #fbfbf8;
    --grass-top: #3f6d24;
    --grass-mid: #6fae33;
    --soil: #b38a5a;
    --machine: #d9a21f;
  }
  * { margin: 0; padding: 0; box-sizing: border-box; }
  html, body {
    width: 929px;
    height: 1200px;
    overflow: hidden;
    background: var(--page-bg);
  }
  .sign {
    position: absolute;
    left: 84px;
    top: 30px;
    width: 760px;
    height: 1140px;
    overflow: hidden;
    background: var(--green-mid);
    box-shadow: 0 4px 18px rgba(0,0,0,0.18);
  }
  .sign__header {
    position: absolute;
    left: 0; top: 0;
    width: 100%;
    height: 230px;
    z-index: 1;
    background: linear-gradient(180deg, var(--green-light) 0%, var(--green-mid) 55%, var(--green-deep) 100%);
    display: flex;
    align-items: center;
    justify-content: center;
    gap: 26px;
    padding-top: 10px;
  }
  .brand__dot {
    width: 92px;
    height: 92px;
    border-radius: 50%;
    background: var(--white);
    flex: none;
  }
  .brand__name {
    font-family: "Oswald", sans-serif;
    font-weight: 600;
    color: var(--white);
    text-transform: uppercase;
    line-height: 1;
    text-align: center;
  }
  .brand__name span { display: block; }
  .brand__name .brand__line1 { font-size: 86px; letter-spacing: 2px; }
  .brand__name .brand__line2 { font-size: 38px; letter-spacing: 3px; margin-top: 8px; }
  .sign__photo {
    position: absolute;
    left: 0; top: 215px;
    width: 100%;
    height: 560px;
    background:
      radial-gradient(ellipse 42% 38% at 72% 28%, var(--machine) 0%, rgba(217,162,31,0.55) 45%, rgba(217,162,31,0) 100%),
      radial-gradient(ellipse 55% 30% at 62% 55%, var(--soil) 0%, rgba(179,138,90,0.5) 50%, rgba(179,138,90,0) 100%),
      linear-gradient(180deg, var(--grass-top) 0%, var(--grass-mid) 45%, var(--green-light) 100%);
  }
  .sign__swoosh {
    position: absolute;
    left: 0; top: 228px;
    width: 100%;
    height: 70px;
    z-index: 2;
  }
  .sign__slogan {
    position: absolute;
    left: 0; top: 672px;
    width: 100%;
    text-align: center;
    font-family: "Oswald", sans-serif;
    font-weight: 700;
    font-size: 64px;
    line-height: 1.3;
    color: var(--white);
    text-transform: uppercase;
    letter-spacing: 1px;
    white-space: nowrap;
    text-shadow: 3px 4px 0 var(--green-ink);
  }
  .sign__phone-band {
    position: absolute;
    left: 0; top: 775px;
    width: 100%;
    height: 160px;
    background: var(--band-white);
    display: flex;
    align-items: center;
    justify-content: center;
  }
  .sign__phone {
    font-family: "Oswald", sans-serif;
    font-weight: 700;
    font-size: 74px;
    line-height: 1;
    white-space: nowrap;
    color: var(--green-ink);
    letter-spacing: 1px;
  }
  .sign__footer {
    position: absolute;
    left: 0; top: 935px;
    width: 100%;
    height: 205px;
    background: linear-gradient(180deg, var(--green-light) 0%, var(--green-mid) 50%, var(--green-deep) 100%);
    display: flex;
    align-items: center;
    justify-content: center;
    gap: 60px;
  }
  .feature {
    display: flex;
    align-items: center;
    gap: 20px;
  }
  .feature__tick { width: 70px; height: 70px; flex: none; }
  .feature__label {
    font-family: "Archivo", sans-serif;
    font-weight: 800;
    font-size: 40px;
    line-height: 1;
    color: var(--white);
    text-transform: uppercase;
    text-shadow: 2px 2px 0 rgba(31,90,44,0.55);
  }
</style>
</head>
<body>
  <main class="sign">
    <div class="sign__photo" role="img" aria-label="Photo of a yellow stump grinder cutting a tree stump in a green lawn, wood chips flying"></div>

    <header class="sign__header">
      <span class="brand__dot" aria-hidden="true"></span>
      <h1 class="brand__name">
        <span class="brand__line1">Barlow's</span>
        <span class="brand__line2">Stump Grinding</span>
      </h1>
    </header>

    <svg class="sign__swoosh" viewBox="0 0 760 70" preserveAspectRatio="none" aria-hidden="true">
      <path d="M0 0 L760 0 L760 8 Q380 60 0 8 Z" fill="#2f9a35"/>
      <path d="M0 8 Q380 60 760 8 L760 22 Q380 78 0 24 Z" fill="#ffffff"/>
    </svg>

    <p class="sign__slogan">No Stump, Too Plump</p>

    <div class="sign__phone-band">
      <p class="sign__phone">CALL: 570-555-0148</p>
    </div>

    <footer class="sign__footer">
      <div class="feature">
        <svg class="feature__tick" viewBox="0 0 70 70" aria-hidden="true">
          <circle cx="35" cy="35" r="32" fill="#ffffff"/>
          <circle cx="35" cy="35" r="26" fill="#1f5a2c"/>
          <path d="M22 36 L32 46 L50 24" fill="none" stroke="#9ccf3c" stroke-width="7" stroke-linecap="round" stroke-linejoin="round"/>
        </svg>
        <p class="feature__label">Fully<br>Insured</p>
      </div>
      <div class="feature">
        <svg class="feature__tick" viewBox="0 0 70 70" aria-hidden="true">
          <circle cx="35" cy="35" r="32" fill="#ffffff"/>
          <circle cx="35" cy="35" r="26" fill="#1f5a2c"/>
          <path d="M22 36 L32 46 L50 24" fill="none" stroke="#9ccf3c" stroke-width="7" stroke-linecap="round" stroke-linejoin="round"/>
        </svg>
        <p class="feature__label">Free<br>Estimates</p>
      </div>
    </footer>
  </main>
</body>
</html>
```